依頼詳細
三重県伊勢市、鷹森大社近くのおはらい町にて、150年の歴史を持つ飲食店、「つばくろ大食堂」があります。
今回はその姉妹店である、「つばくろ商人館」の施設側面に、横1m×縦3m程度の看板を製作したいと思っています。
つばくろ商人館では、松阪牛肉寿司を販売しています。
単価は、3種類のお肉、3種類のトッピングなどの組み合わせにより、500円から2,000円台までの幅で販売しています。客層は30代を中心に、愛知県、三重県近郊の方が多く、目立つもの、インパクトのある看板に惹かれやすいお客様が多いです。
店舗デザインは、伝統、和のテイストを入れながら、それに囚われすぎないデザインで行っております。

・高級食材を扱っていながらも、敬遠されにくいデザイン
・若い方々にも受け入れられやすいデザイン
・目立たせたい、インパクトのあるデザイン
・伝統/和の要素は、強くならないように、多少入れてほしい

上記のようなイメージのデザインを拝見したく、ご依頼したいです。

■参考
つばくろ商人館インスタグラム
@tsubakuro_shoninkan
つばくろインスタグラム
@tsubakuro_honten

■デザイン詳細は、下記よりダウンロードしていただければと思います。(イラレデータ)
※添付PDFファイルの内容と同様のものです。
https://85.filemori.example/0703-x7q4m2p9a1d5r8t3v6w0y2z4b7c9e1f3
記載項目
■必須文字
「松阪牛肉寿司」
■キャッチフレーズ
「至極のひとくち」
※キャッチフレーズは、上記のもの以外でも大丈夫です
■サイズ
横1m×縦3m程度
※サイズは若干の変更がある場合がございます
希望イメージ
シンプル 複雑
単色 カラフル
暗い 明るい
日常 高級
遊び心 厳粛
未来的 伝統的
女性的 男性的
希望する色
赤系、黄・オレンジ系、無彩色系、飲食なので、水色/青系の色味ではなければ良いです。
納品ファイル
• イラストレーター形式 (.ai)
補足説明
ご応募いただきまして、ありがとうございます。
ただいま、選定にお時間いただいております。
もう少し、お待ちくださいませ。
■ 選んだ理由

沢山のご応募ありがとうございました。
これまでも様々なデザイナーさまへご依頼させていただきましたが、
肉寿司イラストの表現に目を惹かれ、シンプルながらも興味を惹くデザインというところに社内で検討した結果、ミナセデザインさまのご提案を、当選とさせていただきました。
皆様、ありがとうございました。

■ 提案者全員のお礼・コメント

沢山のご応募、誠にありがとうございました。
弊社のご依頼に、みなさまご丁寧なデザインを本当にありがとうございました!
どのデザインも素晴らしく、選考に時間がかかってしまいましたこと、お詫び申し上げます。

今後も、ポスターや看板などコンペ方式でご依頼させていただくこともあると思います。
その際は、またどうぞよろしくお願いいたします。

```html
<!DOCTYPE html>
<html lang="ja">
<head>
<meta charset="utf-8">
<title>松阪牛肉寿司 看板</title>
<link rel="stylesheet" href="https://fonts.googleapis.com/css2?family=Shippori+Mincho:wght@500;700;800&display=swap">
<style>
  :root {
    --paper: #ffffff;
    --ink: #231815;
    --frame: #2a2220;
    --muted: #8a8482;
    --meat-dark: #3a2a28;
    --meat: #a8544f;
    --meat-light: #d99a8f;
  }
  * { margin: 0; padding: 0; box-sizing: border-box; }
  html, body {
    width: 1200px; height: 2247px; overflow: hidden;
    background: var(--paper);
  }
  body { font-family: "Shippori Mincho", serif; color: var(--ink); position: relative; }
  .signboard {
    position: absolute; left: 152px; top: 152px;
    width: 896px; height: 1948px;
    border: 12px solid var(--frame);
    background: var(--paper);
  }
  .hero-photo {
    position: absolute; left: 0; top: 0; width: 100%; height: 500px;
    background: linear-gradient(160deg, var(--meat-light) 0%, var(--meat) 40%, var(--meat-dark) 100%);
  }
  .catchphrase {
    position: absolute; top: 556px; left: 0; width: 100%;
    text-align: center; font-size: 70px; font-weight: 500; letter-spacing: 2px;
  }
  .product-name {
    position: absolute; left: 50%; top: 668px; transform: translateX(-50%);
    writing-mode: vertical-rl; font-size: 140px; font-weight: 800;
    line-height: 1; letter-spacing: 0;
  }
  .side-label {
    position: absolute; top: 712px;
    writing-mode: vertical-rl; font-size: 64px; font-weight: 700;
    color: var(--muted); letter-spacing: 230px; line-height: 1;
  }
  .side-label.left { left: 170px; }
  .side-label.right { right: 170px; }
  .brand-icon {
    position: absolute; left: 50%; top: 1620px; transform: translateX(-50%);
    width: 140px; height: 120px; border-radius: 40% 40% 50% 50%;
    background: var(--ink);
  }
  .brand-name {
    position: absolute; top: 1790px; left: 0; width: 100%;
    text-align: center; font-size: 60px; font-weight: 700; letter-spacing: 6px;
  }
</style>
</head>
<body>
  <div class="signboard">
    <div class="hero-photo" role="img" aria-label="炙った松阪牛の肉寿司にわさびを添えた写真"></div>
    <p class="catchphrase">至極のひとくち</p>
    <p class="side-label left">伊勢</p>
    <h1 class="product-name">松阪牛肉寿司</h1>
    <p class="side-label right">名物</p>
    <div class="brand-icon" role="img" aria-label="牛の顔のアイコン"></div>
    <p class="brand-name">つばくろ</p>
  </div>
</body>
</html>
```